Company Business Card Design Project - Revamp the image of an old construction company.

We need a business card designed for a new company in Australia.

Type of business is Commercial Roofing & Painting.

Medium will be brushed black metal card that can/will be acid etched to a brushed steel silver, acid die cut and two printed colours of our choice which will be white and pantone orange.

We have hopes that the design will be simple, modern and represent with a quick glance what our company does.

Please read instructions carefully in must have box any questions please ask.

If you are interested in this job please look at other job that we have which is very similar with logo and design

Please have a look at the things that can be done with metals cards on google images for inspiration.

Target Market(s)

Business owners, commercial property development Men from 25-70 years of age.

Industry/Entity Type

Construction

Requirements
Must have
• Front of card:

Must use the company logo and name provided as attachment (see below norwick vale construction_black_background).

the words -Commercial Painting and Roofing- must be on front of card

details needed on front or back depending on your design

Name
position
email
mobile

all details can be on front with a cool design to be etched on the back of card or to keep front simple you can put all detail on back of card, I will leave the lay out to you.

Colours in logo are

Pantone 144 C Orange
Pantone 11-0601 White
Pantone 7539 C Gray
Pantone 426 C Black

However black will be the base of black metal card. Gray will be replaced with the etching in card revealing the silver. Orange and white will be printed on card.

Please have fun!!
Should not have
• Please don't clutter the card
No fonts smaller then 7 points

```html
<!DOCTYPE html>
<html lang="en">
<head>
<meta charset="utf-8">
<title>Norwick Vale Industries – Business Cards</title>
<link rel="stylesheet" href="https://fonts.googleapis.com/css2?family=Michroma&family=Arimo:wght@400;700&display=swap">
<style>
  :root {
    --page-bg: #d9d6d2;
    --card-dark: #1f1f20;
    --card-mid: #3c3c3e;
    --card-light: #7a7a7c;
    --orange: #f28a1e;
    --silver: #c9c9cb;
    --silver-dim: #9a9a9c;
    --glass-edge: rgba(255,255,255,0.28);
  }
  * { margin: 0; padding: 0; box-sizing: border-box; }
  html, body {
    width: 1200px; height: 1057px; overflow: hidden;
    background: var(--page-bg);
  }
  .sheet {
    position: relative; width: 1200px; height: 1057px;
    display: flex; flex-direction: column; align-items: center;
    justify-content: center; gap: 39px;
  }
  .card {
    position: relative; width: 820px; height: 469px; overflow: hidden;
    background:
      radial-gradient(ellipse 70% 60% at 50% 18%, var(--card-light) 0%, var(--card-mid) 45%, var(--card-dark) 100%);
    box-shadow: 0 6px 18px rgba(0,0,0,0.35);
  }

  /* wordmark */
  .wordmark {
    position: absolute; display: flex; align-items: center; gap: 14px;
    font-family: "Michroma", sans-serif; color: var(--orange);
    text-transform: uppercase; letter-spacing: 0.04em;
  }
  .wordmark .mark-square {
    background: var(--silver-dim);
    flex: none;
  }

  /* front */
  .card-front .wordmark { left: 60px; top: 210px; font-size: 25px; }
  .card-front .wordmark .mark-square { width: 34px; height: 34px; }
  .card-front .tagline {
    position: absolute; left: 60px; top: 272px;
    font-family: "Arimo", sans-serif; font-size: 21px;
    color: var(--silver); letter-spacing: 0.03em;
  }
  .card-front .rule {
    position: absolute; left: 60px; top: 258px; width: 420px; height: 2px;
    background: var(--silver-dim);
  }
  .glass-panel { position: absolute; right: 0; top: 0; width: 330px; height: 469px; }
  .contact {
    position: absolute; left: 530px; top: 110px;
    font-family: "Arimo", sans-serif; color: var(--silver);
  }
  .contact .person-name {
    font-weight: 700; font-size: 30px; color: var(--orange); line-height: 1.1;
  }
  .contact .person-title {
    font-size: 20px; color: var(--silver-dim); margin-bottom: 26px;
  }
  .contact ul { list-style: none; }
  .contact li {
    display: flex; align-items: center; gap: 12px;
    font-size: 19px; letter-spacing: 0.04em; margin-bottom: 14px;
  }
  .contact svg { width: 18px; height: 18px; flex: none; }

  /* back */
  .card-back .wordmark { left: 120px; top: 170px; font-size: 36px; }
  .card-back .wordmark .mark-square { width: 52px; height: 52px; }
  .card-back .rule {
    position: absolute; left: 186px; top: 240px; width: 520px; height: 2px;
    background: var(--silver-dim);
  }
  .card-back .web {
    position: absolute; left: 0; right: 0; top: 320px; text-align: center;
    font-family: "Arimo", sans-serif; font-size: 26px;
    letter-spacing: 0.32em; color: var(--silver-dim);
  }
  .card-back .web strong { color: var(--orange); font-weight: 700; }
</style>
</head>
<body>
<main class="sheet">

  <section class="card card-front" aria-label="Card front">
    <svg class="glass-panel" viewBox="0 0 330 469" aria-hidden="true">
      <defs>
        <linearGradient id="glassFill" x1="0" y1="0" x2="1" y2="1">
          <stop offset="0" stop-color="#ffffff" stop-opacity="0.16"/>
          <stop offset="1" stop-color="#ffffff" stop-opacity="0.03"/>
        </linearGradient>
      </defs>
      <rect x="0" y="0" width="330" height="469" fill="url(#glassFill)"/>
      <line x1="0.5" y1="0" x2="0.5" y2="469" stroke="var(--glass-edge)" stroke-width="2"/>
      <line x1="90" y1="0" x2="90" y2="469" stroke="var(--glass-edge)" stroke-width="1"/>
      <line x1="210" y1="0" x2="210" y2="469" stroke="var(--glass-edge)" stroke-width="1"/>
      <rect x="300" y="0" width="30" height="469" fill="#ffffff" fill-opacity="0.12"/>
    </svg>

    <div class="wordmark"><span class="mark-square"></span><span>Norwick Vale</span></div>
    <div class="rule"></div>
    <p class="tagline">Commercial Painting and Roofing</p>

    <div class="contact">
      <p class="person-name">Your Name</p>
      <p class="person-title">Title</p>
      <ul>
        <li>
          <svg viewBox="0 0 18 18"><circle cx="9" cy="9" r="8" fill="none" stroke="var(--orange)" stroke-width="1.6"/><path d="M6 5c0 4 3 7 7 7l-1.5 1.6C8 13 5 10 4.5 6.5z" fill="var(--orange)"/></svg>
          012-345-6789
        </li>
        <li>
          <svg viewBox="0 0 18 18"><rect x="1" y="4" width="16" height="11" fill="var(--orange)"/><path d="M1 4l8 6 8-6" fill="none" stroke="var(--card-dark)" stroke-width="1.4"/></svg>
          name@norwickvale.com
        </li>
        <li>
          <svg viewBox="0 0 18 18"><circle cx="9" cy="9" r="8" fill="none" stroke="var(--orange)" stroke-width="1.6"/><ellipse cx="9" cy="9" rx="3.5" ry="8" fill="none" stroke="var(--orange)" stroke-width="1.2"/><line x1="1" y1="9" x2="17" y2="9" stroke="var(--orange)" stroke-width="1.2"/></svg>
          www.norwickvale.com
        </li>
      </ul>
    </div>
  </section>

  <section class="card card-back" aria-label="Card back">
    <div class="wordmark"><span class="mark-square"></span><span>Norwick Vale</span></div>
    <div class="rule"></div>
    <p class="web">www.<strong>norwickvale</strong>.com</p>
  </section>

</main>
</body>
</html>
```